DPW Business Card

This is a wide-range political consulting firm specializing in high-profile political campaigns. Red should be a predominant color in the business card, since this is a Lantern Party inspired consulting firm, but the word "lantern" will not appear anywhere in any kind of literature. Look has to be clean and crisp. The design should be forward thinking and appropriate for a company that is trying to break away from a traditionally "stodgy" image in politics.

Target Market(s)

potential national political candidates, wealthy donors,

Industry/Entity Type

Political

Contact Information for Business Card

Doran P. Whitcliffe
Political Consultant
437 Orchard Lane SE
#358
Washington, DC 20417

```html
<!DOCTYPE html>
<html lang="en">
<head>
<meta charset="utf-8">
<title>Doran P. Whitcliffe — Business Card</title>
<link rel="stylesheet" href="https://fonts.googleapis.com/css2?family=Allura&family=Questrial&display=swap">
<style>
  :root {
    --backdrop: #e9e4df;
    --red-deep: #8a0000;
    --red-mid: #c80000;
    --red-bright: #ff0000;
    --ink-light: #ffffff;
  }
  html, body {
    margin: 0;
    padding: 0;
    width: 1200px;
    height: 1000px;
    overflow: hidden;
    background: var(--backdrop);
  }
  .canvas {
    position: relative;
    width: 1200px;
    height: 1000px;
  }
  .business-card {
    position: absolute;
    left: 70px;
    top: 190px;
    width: 1060px;
    height: 620px;
    border-radius: 44px;
    overflow: hidden;
    background: var(--red-mid);
    box-shadow: 0 18px 40px rgba(0, 0, 0, 0.18);
  }
  .card-shapes {
    position: absolute;
    inset: 0;
    width: 100%;
    height: 100%;
  }
  .shape-side { fill: var(--red-deep); }
  .shape-diamond { fill: var(--red-bright); }
  .card-text {
    position: absolute;
    left: 0;
    right: 0;
    top: 0;
    color: var(--ink-light);
    text-align: center;
  }
  .holder-name {
    position: absolute;
    left: 0;
    right: 0;
    top: 208px;
    margin: 0;
    font-family: "Allura", cursive;
    font-weight: 400;
    font-size: 118px;
    line-height: 1;
    letter-spacing: 1px;
  }
  .name-rule {
    position: absolute;
    left: 170px;
    width: 760px;
    top: 346px;
    height: 2px;
    background: var(--ink-light);
  }
  .holder-title {
    position: absolute;
    left: 0;
    right: 0;
    top: 358px;
    margin: 0;
    font-family: "Questrial", sans-serif;
    font-size: 36px;
    font-weight: 400;
  }
  .holder-address {
    position: absolute;
    left: 0;
    right: 0;
    top: 408px;
    margin: 0;
    font-family: "Questrial", sans-serif;
    font-size: 23px;
    font-style: normal;
  }
</style>
</head>
<body>
  <main class="canvas">
    <section class="business-card">
      <svg class="card-shapes" viewBox="0 0 530 310" preserveAspectRatio="none" aria-hidden="true">
        <polygon class="shape-side" points="0,12 128,155 0,298"/>
        <polygon class="shape-side" points="530,12 402,155 530,298"/>
        <polygon class="shape-diamond" points="30,155 200,0 360,0 502,155 360,310 200,310"/>
      </svg>
      <div class="card-text">
        <h1 class="holder-name">Doran P. Whitcliffe</h1>
        <div class="name-rule"></div>
        <p class="holder-title">Political Consultant</p>
        <address class="holder-address">437 Orchard Lane SE #358 Washington, DC 20417</address>
      </div>
    </section>
  </main>
</body>
</html>
```